BrindleCrewing Business Card Design

We are a staffing company finding positions for dedicated nurses and physicians.

Target Market(s)

Business Professionals

Industry/Entity Type

Staffing

Contact Information for Business Card

Gerald Pinkney
Chairman
417 39th Lantern West
SAINT PETERSBURG FL 33703
813-472-6158 Mobile
813-690-4137 Fax
gpinkney@brindlecrewing.com
www.brindlecrewing.com

Font styles to use
Sans Serif

Colors
fbee3e
f04a50
f37122

Requirements
Must have
• Logo Attached, see colors below. We'd like to see Yellow, Orange and Red.

```html
<!DOCTYPE html>
<html lang="en">
<head>
<meta charset="utf-8">
<title>BrindleCrewing Business Card</title>
<link rel="stylesheet" href="https://fonts.googleapis.com/css2?family=Poppins:wght@600;700&family=Questrial&display=swap">
<style>
  :root {
    --bg: #dedede;
    --card-front: #e8e8e8;
    --yellow: #fbee3e;
    --orange: #f37122;
    --red: #f04a50;
    --grey-text: #555555;
    --white-text: #ffffff;
  }
  * { margin: 0; padding: 0; box-sizing: border-box; }
  html, body {
    width: 1200px; height: 1200px; overflow: hidden;
    background: var(--bg);
  }
  .stage { position: relative; width: 1200px; height: 1200px; }
  .card {
    position: absolute; left: 227px; width: 746px; height: 425px;
    overflow: hidden;
  }
  .card--front { top: 135px; background: var(--card-front); }
  .card--back {
    top: 640px;
    background: linear-gradient(90deg, var(--yellow) 0%, #f7b02f 22%, var(--orange) 50%, #f15c3a 76%, var(--red) 100%);
  }
  .wordmark {
    position: absolute; font-family: "Poppins", sans-serif; font-weight: 700;
    letter-spacing: -2px; line-height: 1; white-space: nowrap;
  }
  .card--front .wordmark { left: 33px; top: 60px; font-size: 66px; color: var(--orange); }
  .card--back .wordmark {
    left: 0; right: 0; top: 180px; text-align: center;
    font-size: 70px; color: var(--white-text);
  }
  .person { position: absolute; left: 36px; top: 226px; }
  .person__name {
    font-family: "Poppins", sans-serif; font-weight: 600; font-size: 22px; line-height: 1.1;
  }
  .person__first { color: var(--orange); }
  .person__last { color: var(--red); }
  .person__title {
    font-family: "Questrial", sans-serif; font-size: 17.5px; color: var(--grey-text); margin-top: 2px;
  }
  .contacts { position: absolute; left: 35px; top: 303px; list-style: none; }
  .contacts li {
    display: flex; align-items: center; height: 22.4px;
    font-family: "Questrial", sans-serif; font-size: 17.5px; color: var(--grey-text);
  }
  .contacts svg { width: 16px; height: 16px; margin-right: 9px; flex: none; fill: var(--orange); }
  .contacts .icon-line { fill: none; stroke: var(--orange); stroke-width: 1.6; }
  .contacts .icon-cut { fill: var(--card-front); }
  .contacts .icon-cut-line { fill: none; stroke: var(--card-front); stroke-width: 1.3; }
  .address {
    position: absolute; left: 374px; top: 351px; font-style: normal;
    font-family: "Questrial", sans-serif; font-size: 17.5px; line-height: 22.4px; color: var(--grey-text);
  }
</style>
</head>
<body>
<main class="stage">
  <section class="card card--front">
    <div class="wordmark">BrindleCrewing</div>
    <div class="person">
      <div class="person__name"><span class="person__first">Gerald</span> <span class="person__last">Pinkney</span></div>
      <div class="person__title">Chairman</div>
    </div>
    <ul class="contacts">
      <li>
        <svg viewBox="0 0 16 16" aria-hidden="true"><path d="M1 6c0-2 3-3 7-3s7 1 7 3v1h-4V5.5H5V7H1z"/><path d="M4 8h8l2 5H2z"/><circle class="icon-cut" cx="8" cy="10.5" r="1.6"/></svg>
        813-472-6158
      </li>
      <li>
        <svg viewBox="0 0 16 16" aria-hidden="true"><rect x="1" y="6" width="14" height="9" rx="1"/><rect class="icon-line" x="4" y="1" width="8" height="6"/><rect class="icon-cut" x="4" y="9" width="8" height="1.2"/><rect class="icon-cut" x="4" y="11.5" width="8" height="1.2"/></svg>
        813-690-4137
      </li>
      <li>
        <svg viewBox="0 0 16 16" aria-hidden="true"><rect class="icon-line" x="1" y="3" width="14" height="10"/><path class="icon-line" d="M1.5 3.5L8 9l6.5-5.5"/></svg>
        gpinkney@brindlecrewing.com
      </li>
      <li>
        <svg viewBox="0 0 16 16" aria-hidden="true"><circle cx="8" cy="8" r="7"/><path class="icon-cut-line" d="M4 4c2 0 3 1 2 3s1 2 0 4M10 3c0 2 2 2 3 3M11 10c1 0 2 1 1 3"/></svg>
        www.brindlecrewing.com
      </li>
    </ul>
    <address class="address">
      417 39th Lantern West<br>
      SAINT PETERSBURG FL 33703
    </address>
  </section>

  <section class="card card--back">
    <div class="wordmark">BrindleCrewing</div>
  </section>
</main>
</body>
</html>
```